Need a book cover design for book titled: Resting Beside the River--Simple Methods for the Crossing

This book describes and presents tools to connect with and activate the Lightbody that we all carry within us. It talks about the Lighbody, brief history, lightbody levels and offers exercises to bring light into the body.
I envision a design that shows a physical body changing into light /surrounded by light; a resurrected body ascending to higher dimensions of Spirit o anything comparable .
Updates

Target Market(s)

Mature audience of spiritual seekers and those on spiritual path

Requirements
Must have
• Space on backcover for book summary at top and title and author name on spine.

```html
<!DOCTYPE html>
<html lang="en">
<head>
<meta charset="utf-8">
<title>Resting Beside the River — Book Cover</title>
<link rel="stylesheet" href="https://fonts.googleapis.com/css2?family=Montserrat:wght@300;400&display=swap">
<style>
  :root {
    --backdrop: #e7dee7;
    --cover-top: #9c4a5c;
    --cover-upper: #b87878;
    --cover-mid: #d7a08e;
    --cover-low: #eab57c;
    --cover-bottom: #f2c77e;
    --glow: #ffffff;
    --title-ink: #ffffff;
    --author-ink: #6e2a3c;
  }
  html, body {
    margin: 0;
    padding: 0;
    width: 1200px;
    height: 843px;
    overflow: hidden;
    background: var(--backdrop);
  }
  .canvas {
    position: relative;
    width: 1200px;
    height: 843px;
  }
  .book-cover {
    position: absolute;
    left: 372px;
    top: 42px;
    width: 456px;
    height: 760px;
    overflow: hidden;
    font-family: "Montserrat", sans-serif;
    box-shadow: 0 18px 40px rgba(80, 50, 80, 0.18);
  }
  .cover-art {
    position: absolute;
    inset: 0;
    background: linear-gradient(180deg,
      var(--cover-top) 0%,
      var(--cover-upper) 22%,
      var(--cover-mid) 48%,
      var(--cover-low) 75%,
      var(--cover-bottom) 100%);
  }
  .cover-art::after {
    content: "";
    position: absolute;
    inset: 0;
    background: radial-gradient(ellipse 46% 36% at 62% 62%,
      rgba(255,255,255,0.95) 0%,
      rgba(255,255,255,0.7) 30%,
      rgba(255,255,255,0.25) 60%,
      rgba(255,255,255,0) 100%);
  }
  .cover-title {
    position: absolute;
    left: 22px;
    top: 34px;
    margin: 0;
    color: var(--title-ink);
    font-weight: 300;
    font-size: 40px;
    line-height: 1.1;
    letter-spacing: 0.5px;
    text-transform: uppercase;
  }
  .cover-subtitle {
    position: absolute;
    left: 22px;
    top: 138px;
    margin: 0;
    color: var(--title-ink);
    font-weight: 300;
    font-size: 17px;
    letter-spacing: 0.3px;
  }
  .cover-author {
    position: absolute;
    left: 22px;
    bottom: 30px;
    margin: 0;
    color: var(--author-ink);
    font-weight: 400;
    font-size: 22px;
  }
</style>
</head>
<body>
  <main class="canvas">
    <article class="book-cover">
      <div class="cover-art" role="img" aria-label="Photograph of a figure in silhouette leaning back with arms outstretched, dissolving into a burst of light against a rose-to-gold sunset sky"></div>
      <h1 class="cover-title">Resting Beside<br>the River</h1>
      <p class="cover-subtitle">Simple Methods for the Crossing</p>
      <p class="cover-author">Autor Name</p>
    </article>
  </main>
</body>
</html>
```